Create design for Dark Theme Website

We are a solar company wanting a website that has clean crisp feel of Pearfield. We like the dark contrasting theme in the Vorlan Cellbank and Brightmoor House Charge websites listed below. We want a dark theme with single scroll down style page.
See the following for theme and look:
https://www.vorlan-example.com/sunarrays
https://brightmoorhousecharge-example.com/

Our current website for further information is http://quillstonesun-example.co.nz

We want the following sections on the single page as they scroll down:
1. Main Landing page for Quill Stone Solar.
2. About us - company / service description
3. How it works - animation showing house with powerlines. The animations will show 'on-grid' day time, on-grid night time, Hybrid day time, Hybrid nightime / or stormy weather)
4. Mobile / monitoring - We like the brightmoor photo style. We want to show our app on phone.
5. Home installation location - SHow location of installation and details about requirements
6. Solution Specifications Section- A button product filter, basic specs are shown on site (like vorlan buy now) - really detailed information on brochure (like brightmoor size selection)
7. Request Solutions Consultant form - if you want a quote, done in form style (Name, email, phone)
8. Estimator - (price estimator like vorlan buy now) would have address finder, home bedroom count, install timeframe, contact details (first name, last name, email, phone, contact time preference)

I have uploaded our two brochures and some example diagrams for reference and image material.

Target Market(s)

Solar Energy Customers, wanting ongrid, off-grid or hybrid microgrids or solar energy solutions.

Industry/Entity Type

Solar Energy

Coding

Number of Pages Required

Font styles to use
Sans Serif

Requirements
Must have
• The dark theme to match the company name and themes used by Vorlan and Brightmoor. Want a single scroll down page
Nice to have
• Nice transitions and animations to show different types of microgrid.

```html
<!DOCTYPE html>
<html lang="en">
<head>
<meta charset="utf-8">
<title>Quill Stone Solar</title>
<link rel="stylesheet" href="https://fonts.googleapis.com/css2?family=Poppins:wght@400;500;600&display=swap">
<style>
:root{
  --green:#6aa51f;
  --green-dark:#5c921a;
  --ink:#ffffff;
  --muted:#e6e6e6;
  --nav:#252a33;
  --about-bg:#222222;
  --how-bg:#333333;
  --circle:#434343;
  --app-bg:#232323;
}
*{box-sizing:border-box;margin:0;padding:0}
html,body{width:809px;height:1200px;overflow:hidden}
body{position:relative;background:var(--about-bg);font-family:"Poppins",sans-serif;color:var(--ink)}
.abs{position:absolute}

.topbar{left:0;top:0;width:809px;height:25px;background:var(--green);font-size:8.5px;font-weight:600;text-transform:uppercase}
.topbar .links{left:101px;top:7px;display:flex;gap:21px}
.topbar .contact{right:101px;top:6px;display:flex;gap:16px;align-items:center;text-transform:none;font-weight:500}
.topbar .contact span{display:flex;align-items:center;gap:6px}

.hero{left:0;top:0;width:809px;height:475px;
  background:linear-gradient(172deg,#6f8395 0%,#8a98a2 30%,#55677a 55%,#2c3b63 70%,#1f2c55 100%)}
.navbar{left:0;top:25px;width:809px;height:46px;background:rgba(37,42,51,.88)}
.brand{left:101px;top:11px;font-size:11px;font-weight:500;line-height:12px;letter-spacing:.5px;display:flex;align-items:center;gap:6px}
.brand .mark{width:9px;height:9px;background:var(--ink)}
.menu{right:101px;top:18px;display:flex;gap:21px;font-size:8.5px;font-weight:600;text-transform:uppercase}
.hero-title{left:100px;top:201px;font-size:26px;font-weight:600;white-space:nowrap}
.hero-lead{left:101px;top:243px;width:580px;font-size:15.5px;line-height:23px;font-weight:400}
.btn{height:30px;width:101px;font-size:7.5px;font-weight:600;text-transform:uppercase;display:flex;align-items:center;justify-content:center}
.btn-solid{left:101px;top:312px;background:var(--green)}
.btn-ghost{left:210px;top:312px;border:1.5px solid var(--green)}

.about{left:0;top:475px;width:809px;height:166px;background:var(--about-bg)}
.section-heading{font-size:17px;font-weight:600;text-transform:uppercase}
.about h2{left:101px;top:47px}
.about p{left:314px;top:48px;width:400px;font-size:9.3px;line-height:13.6px}

.how{left:0;top:641px;width:809px;height:337px;background:var(--how-bg);text-align:center}
.how h2{left:0;top:45px;width:809px}
.how .intro{left:0;top:75px;width:809px;font-size:9.5px;line-height:13.6px}
.step{top:124px;width:180px;margin-left:-90px}
.step .icon{width:76px;height:76px;border-radius:50%;background:var(--circle);margin:0 auto;display:flex;align-items:center;justify-content:center}
.step h3{margin-top:10px;font-size:13.3px;font-weight:600;white-space:nowrap}
.step p{margin-top:6px;font-size:9.5px;line-height:13.6px;padding:0 12px}

.app{left:0;top:978px;width:809px;height:222px;background:var(--app-bg)}
.app .phone{left:10px;top:47px;width:280px;height:134px;border-radius:14px;
  background:radial-gradient(ellipse at 50% 50%,#7cb43a 0%,#5d9a1e 55%,#2b2b2b 100%)}
.app h2{left:314px;top:49px;width:420px;line-height:23px}
.app p{left:316px;top:108px;width:400px;font-size:9.3px;line-height:13.6px}
</style>
</head>
<body>

<div class="abs hero" role="img" aria-label="Photo of solar panel rows under a cloudy blue sky"></div>

<header>
  <div class="abs topbar">
    <nav class="abs links"><span>Quote</span><span>Estimate</span></nav>
    <div class="abs contact">
      <span>
        <svg width="13" height="13" viewBox="0 0 24 24" fill="#fff" aria-hidden="true"><path d="M6.6 10.8a15 15 0 006.6 6.6l2.2-2.2a1 1 0 011-.25 11.4 11.4 0 003.6.57 1 1 0 011 1V20a1 1 0 01-1 1A17 17 0 013 4a1 1 0 011-1h3.5a1 1 0 011 1c0 1.25.2 2.45.57 3.57a1 1 0 01-.25 1z"/></svg>
        0299 480 316
      </span>
      <span>
        <svg width="14" height="11" viewBox="0 0 24 18" fill="none" stroke="#fff" stroke-width="2" aria-hidden="true"><rect x="1" y="1" width="22" height="16"/><path d="M1 1l11 9 11-9"/></svg>
        hello@quillstonesun-example.co.nz
      </span>
    </div>
  </div>
  <div class="abs navbar">
    <div class="abs brand"><span class="mark"></span><span>Quill Stone Solar</span></div>
    <nav class="abs menu">
      <span>Home</span><span>About</span><span>How it works</span><span>Monitoring</span><span>Installation</span><span>Solution</span>
    </nav>
  </div>
</header>

<section class="hero-content">
  <h1 class="abs hero-title">Northland's Off Grid Technology Specialists</h1>
  <p class="abs hero-lead">Servicing the great Far North of New Zealand. We are happy to provide you the most current advice on power solutions and maintance packages.</p>
  <span class="abs btn btn-solid">Request Quote</span>
  <span class="abs btn btn-ghost">Learn More</span>
</section>

<section class="abs about">
  <h2 class="abs section-heading">About Us</h2>
  <p class="abs">After 20+ years of designing, building and installing world leading, award winning and mission critical electrical and electronic solutions around the world. The management team at Quill Stone Solar are now offering 'Turn-Key' energy storage solutions for the Bay of Islands and Northland. We are passionate about renewable energy and believe in solutions that protect our environment.</p>
</section>

<section class="abs how">
  <h2 class="abs section-heading">How it works</h2>
  <p class="abs intro">Fusce a diam rhoncus nisi mollis cursus. Sed facilisis<br>tellus et nibh interdum tristique. Proin posuere est odio.</p>

  <div class="abs step" style="left:175px">
    <div class="icon">
      <svg width="42" height="36" viewBox="0 0 42 36" fill="var(--green)" aria-hidden="true">
        <circle cx="33" cy="8" r="4"/>
        <path d="M2 20l12-9h16l-8 9z"/><rect x="2" y="20" width="18" height="15"/>
        <path d="M22 20l8-9 9 9v15H22z"/><rect x="28" y="26" width="5" height="9" fill="var(--circle)"/>
      </svg>
    </div>
    <h3>Store Energy Day-Time</h3>
    <p>Pellentesque ut commodo ipsum. Mauris velit lectus, dignissim a nibh sit amet, semper posuere purus.</p>
  </div>

  <div class="abs step" style="left:404px">
    <div class="icon">
      <svg width="42" height="40" viewBox="0 0 42 40" fill="none" stroke="var(--green)" stroke-width="2" aria-hidden="true">
        <rect x="22" y="2" width="18" height="18" fill="var(--green)" stroke="none"/>
        <circle cx="31" cy="11" r="5" stroke="var(--circle)"/>
        <path d="M5 4v6M11 4v6"/><rect x="2" y="10" width="12" height="10" fill="var(--green)" stroke="none"/>
        <path d="M8 20v14h32"/>
      </svg>
    </div>
    <h3>Use Energy Night-Time</h3>
    <p>Pellentesque ut commodo ipsum. Mauris velit lectus, dignissim a nibh sit amet, semper posuere purus.</p>
  </div>

  <div class="abs step" style="left:632px">
    <div class="icon">
      <svg width="42" height="30" viewBox="0 0 42 30" fill="var(--green)" aria-hidden="true">
        <ellipse cx="24" cy="5" rx="8" ry="3"/><ellipse cx="24" cy="11" rx="8" ry="3"/>
        <ellipse cx="32" cy="18" rx="9" ry="3"/><ellipse cx="32" cy="25" rx="9" ry="3"/>
        <circle cx="10" cy="18" r="9"/>
        <text x="10" y="22.5" font-size="12" font-family="Poppins,sans-serif" font-weight="600" text-anchor="middle" fill="var(--circle)">$</text>
      </svg>
    </div>
    <h3>Sell Energy on-Demand</h3>
    <p>Pellentesque ut commodo ipsum. Mauris velit lectus, dignissim a nibh sit amet, semper posuere purus.</p>
  </div>
</section>

<section class="abs app">
  <div class="abs phone" role="img" aria-label="Smartphone showing the monitoring app in green"></div>
  <h2 class="abs section-heading">Lorem ipsum dolor sit amet, consectetur elit. Aenean eget felis ex. Aenean quis risu</h2>
  <p class="abs">Mauris hendrerit sed odio vel sollicitudin. Aliquam facilisis sapien in semper facilisis. Suspendisse hendrerit orci lorem, sit amet sollicitudin eros pellentesque vel. Pellentes ornare, nulla eu tincidunt sagittis, risus lorem pulvinar arcu, ut tempor purus augue vulputate lectus.</p>
</section>

</body>
</html>
```